Larkspur IP Access Control Data Sheet

Initially we are looking for a better and consistent ( cleaner / corporate) layout / design of the attached A4 Data Sheet and A5 mini flyer. Going forward we would then be looking to create a Brochure & flyers and some other items ( wall displays, banners etc.)
Target Market(s)
Our customers are end -users and security equipment installers
Industry/Entity Type
Cleaner
Font styles to use
Sans Serif
Requirements
Must have
- 1. Better images of devices ( pc, laptop , tablet, smartphone etc.) with clearer screen shots of the software
- 2. A consistent them across all literature
- 3. Designs must be print ready and in an editable format (PSD , GIMP etc.)

```html
<!DOCTYPE html>
<html lang="en">
<head>
<meta charset="utf-8">
<title>Larkspur IP – E-Mail Settings</title>
<link href="https://fonts.googleapis.com/css2?family=Source+Sans+3:wght@400;600&display=swap" rel="stylesheet">
<style>
  :root{
    --page:#ffffff;
    --header:#cccccc;
    --sidebar:#f7f7f7;
    --rule:#dcdcdc;
    --faded:#b4b4b4;
    --modal-head:#666666;
    --modal-body:#e4e4e4;
    --modal-edge:#bdbdbd;
    --green:#3aad34;
    --dark:#2f2f2f;
    --field:#ffffff;
    --ghost-field:#e6e6e6;
    --ink:#111111;
    --t-home:#bfe3b9;
    --t-report:#fbf0c2;
    --t-users:#e4bbe0;
    --t-cat:#d6b4dc;
    --t-time:#d2d2d2;
    --t-door:#c2c5e5;
    --t-holiday:#b1e6e7;
    --t-rel:#cfbbdf;
    --t-more:#b9cdea;
  }
  *{box-sizing:border-box;margin:0;padding:0}
  html,body{width:1200px;height:1200px;overflow:hidden;background:var(--page);
    font-family:"Source Sans 3",sans-serif}
  .app{position:relative;width:1200px;height:1200px;overflow:hidden}
  .abs{position:absolute}

  .app-header{left:0;top:0;width:1200px;height:120px;background:var(--header)}
  .brand-mark{left:26px;top:14px;width:88px;height:88px;border:3px solid #fff}
  .brand-name{left:130px;top:30px;color:#fff;font-size:50px;font-weight:400;letter-spacing:2px;line-height:1}
  .brand-tag{left:132px;top:82px;color:#fff;font-size:19px;line-height:1}

  .sidebar{left:0;top:120px;width:461px;height:1080px;background:var(--sidebar)}
  .nav-item{left:59px;width:391px;height:106px;border-bottom:2px solid var(--rule)}
  .nav-tile{position:absolute;left:0;top:10px;width:90px;height:86px;display:flex;align-items:center;justify-content:center}
  .nav-tile svg{width:56px;height:56px}
  .nav-label{position:absolute;left:120px;top:30px;font-size:36px;color:var(--faded);line-height:1;white-space:nowrap}

  .ghost-tile{left:486px;top:133px;width:168px;height:90px;background:var(--t-report)}
  .ghost-title{left:676px;top:150px;font-size:90px;color:#e6e6e6;font-weight:600;line-height:1}

  .modal{left:292px;top:194px;width:908px;height:488px;background:var(--modal-body);
    border-left:8px solid var(--modal-edge);border-bottom:8px solid var(--modal-edge)}
  .modal-head{position:absolute;left:0;top:0;width:100%;height:144px;background:var(--modal-head)}
  .modal-icon{position:absolute;left:15px;top:16px;width:118px;height:113px;background:var(--green);
    display:flex;align-items:center;justify-content:center}
  .modal-title{position:absolute;left:154px;top:40px;color:#fff;font-size:54px;font-weight:600;line-height:1}
  .field-label{position:absolute;top:194px;font-size:38px;font-weight:600;color:var(--ink);line-height:1}
  .field{position:absolute;top:259px;width:396px;height:58px;background:var(--field);
    font-size:24px;color:var(--ink);padding:15px 20px;line-height:1.2}
  .btn{position:absolute;top:410px;height:50px;font-size:36px;color:#fff;line-height:50px;text-align:center}
  .btn-save{left:17px;width:102px;background:var(--green)}
  .btn-back{left:139px;width:102px;background:var(--dark)}

  .ghost-field{background:var(--ghost-field);color:var(--faded);font-size:29px;padding:4px 14px;line-height:1.2}
  .ghost-text{color:var(--faded);font-size:29px;line-height:1;white-space:nowrap}
</style>
</head>
<body>
<div class="app">

  <header class="app-header abs">
    <div class="brand-mark abs"></div>
    <div class="brand-name abs">LARKSPUR IP</div>
    <div class="brand-tag abs">DOOR ACCESS CONTROL SYSTEM</div>
  </header>

  <nav class="sidebar abs">
    <div class="nav-item abs" style="top:0">
      <div class="nav-tile" style="background:var(--t-home)">
        <svg viewBox="0 0 56 56"><path d="M28 6 4 28h7v22h13V36h8v14h13V28h7z" fill="#fff"/></svg>
      </div><span class="nav-label">Home</span>
    </div>
    <div class="nav-item abs" style="top:106px">
      <div class="nav-tile" style="background:var(--t-report)">
        <svg viewBox="0 0 56 56"><rect x="6" y="30" width="12" height="20" fill="#fff"/><rect x="22" y="18" width="12" height="32" fill="#fff"/><rect x="38" y="8" width="12" height="42" fill="#fff"/></svg>
      </div><span class="nav-label">Report</span>
    </div>
    <div class="nav-item abs" style="top:212px">
      <div class="nav-tile" style="background:var(--t-users)">
        <svg viewBox="0 0 56 56"><circle cx="28" cy="18" r="12" fill="#fff"/><path d="M4 54c0-14 10-22 24-22s24 8 24 22z" fill="#fff"/></svg>
      </div><span class="nav-label">Users</span>
    </div>
    <div class="nav-item abs" style="top:318px">
      <div class="nav-tile" style="background:var(--t-cat)">
        <svg viewBox="0 0 56 56" fill="#fff"><circle cx="15" cy="10" r="7"/><path d="M2 28c0-8 6-12 13-12s13 4 13 12z"/><circle cx="41" cy="10" r="7"/><path d="M28 28c0-8 6-12 13-12s13 4 13 12z"/><circle cx="15" cy="36" r="7"/><path d="M2 54c0-8 6-12 13-12s13 4 13 12z"/><circle cx="41" cy="36" r="7"/><path d="M28 54c0-8 6-12 13-12s13 4 13 12z"/></svg>
      </div><span class="nav-label">Category</span>
    </div>
    <div class="nav-item abs" style="top:424px">
      <div class="nav-tile" style="background:var(--t-time)">
        <svg viewBox="0 0 56 56"><circle cx="28" cy="28" r="23" fill="none" stroke="#fff" stroke-width="5"/><path d="M28 13v16h12" fill="none" stroke="#fff" stroke-width="5"/></svg>
      </div><span class="nav-label">Time Zone</span>
    </div>
    <div class="nav-item abs" style="top:530px">
      <div class="nav-tile" style="background:var(--t-door)">
        <svg viewBox="0 0 56 56"><path d="M10 10 44 2v52L10 46z" fill="#fff"/></svg>
      </div><span class="nav-label">Door Groups</span>
    </div>
    <div class="nav-item abs" style="top:636px">
      <div class="nav-tile" style="background:var(--t-holiday)">
        <svg viewBox="0 0 56 56"><path d="M50 6c-3-3-8 0-11 3l-9 9-22-6-5 5 18 11-8 8-8-1-3 3 9 5 5 9 3-3-1-8 8-8 11 18 5-5-6-22 9-9c3-3 6-8 3-11z" fill="#fff"/></svg>
      </div><span class="nav-label">Holiday</span>
    </div>
    <div class="nav-item abs" style="top:742px">
      <div class="nav-tile" style="background:var(--t-rel)">
        <svg viewBox="0 0 56 56" fill="none" stroke="#fff" stroke-width="4"><rect x="4" y="14" width="30" height="14" rx="7" transform="rotate(45 19 21)"/><rect x="22" y="28" width="30" height="14" rx="7" transform="rotate(45 37 35)"/></svg>
      </div><span class="nav-label">Relationship</span>
    </div>
    <div class="nav-item abs" style="top:848px;border-bottom:none">
      <div class="nav-tile" style="background:var(--t-more)"></div>
    </div>
  </nav>

  <div class="ghost-tile abs"></div>
  <div class="ghost-title abs">SMTP Settings</div>

  <div class="ghost-field abs" style="left:481px;top:689px;width:289px;height:48px">smtp.relayhost.net</div>
  <div class="ghost-field abs" style="left:832px;top:689px;width:326px;height:48px">sam@larkspurhq.co.uk</div>
  <div class="ghost-text abs" style="left:496px;top:786px">Lkaccess Network Setting</div>
  <div class="ghost-text abs" style="left:496px;top:876px">MAC Address</div>
  <div class="ghost-text abs" style="left:785px;top:876px">IP Type</div>
  <div class="ghost-text abs" style="left:962px;top:876px">IP Address</div>
  <div class="ghost-text abs" style="left:1154px;top:876px">Net</div>
  <div class="abs" style="left:481px;top:913px;width:287px;height:57px;background:var(--ghost-field)"></div>
  <div class="abs" style="left:776px;top:913px;width:130px;height:57px;background:var(--ghost-field)"></div>

  <section class="modal abs" aria-label="E-Mail Settings">
    <div class="modal-head">
      <div class="modal-icon">
        <svg width="86" height="86" viewBox="0 0 86 86"><path d="M30 6a20 20 0 0 0-20 26L6 28l-2 6 8 8a20 20 0 0 0 22-4l38 38a7 7 0 0 0 10-10L44 28a20 20 0 0 0-4-22l-8 8-8-2-2-8z" fill="#fff"/><circle cx="75" cy="74" r="3" fill="var(--green)"/></svg>
      </div>
      <h1 class="modal-title">E-Mail Settings</h1>
    </div>
    <label class="field-label" style="left:26px">SMTP Server</label>
    <label class="field-label" style="left:492px">User Account</label>
    <div class="field" style="left:15px">mail.relayhost.net</div>
    <div class="field" style="left:484px;padding-left:12px">ops@larkspurhq.co.uk</div>
    <div class="btn btn-save">Save</div>
    <div class="btn btn-back">Back</div>
  </section>

</div>
</body>
</html>
```